Design my business card

I require a business card design ready to send to a professional printers.

here are the requirements:
- please use the below link as a rough guide
- dimensions are 85mm x 55mm, with safety space around it
- please use any sample value for the name/email/etc. I'll pass the real details on to the winner.
- I need two versions, with blue and orange, per the attached images

In order to be accepted for this context, please quote X974 in your response. Entry costs accepted are below 40 euro only. Anything above 40 euro or not quoting the text are rejected sorry!

I can attach adobe illustrator version of the logo if its needed

```html
<!DOCTYPE html>
<html lang="en">
<head>
<meta charset="utf-8">
<title>veranode — business card</title>
<link rel="stylesheet" href="https://fonts.googleapis.com/css2?family=Open+Sans:wght@400;600&display=swap">
<style>
  :root {
    --stage: #3a3b3d;
    --blue: #4351a5;
    --orange: #ea9128;
    --ink: #16181f;
    --accent-blue: #2b7fc1;
    --rule-blue: #2f78b8;
    --white: #ffffff;
    --text: #2a2b30;
  }
  * { margin: 0; padding: 0; box-sizing: border-box; }
  html, body { width: 1200px; height: 900px; overflow: hidden; }
  body {
    background: var(--stage);
    font-family: "Open Sans", Arial, sans-serif;
    position: relative;
  }
  .card {
    position: absolute;
    width: 600px;
    height: 388px;
    overflow: hidden;
  }
  .wordmark {
    position: absolute;
    left: 0; width: 100%;
    text-align: center;
    color: var(--ink);
    font-weight: 400;
    font-size: 80px;
    letter-spacing: -1px;
    line-height: 1;
  }
  /* front */
  .card--front {
    left: 300px; top: 40px;
    background: var(--blue);
  }
  .card--front .wordmark { top: 120px; }
  .front-web {
    position: absolute;
    right: 130px; top: 272px;
    display: flex; align-items: center; gap: 8px;
    font-size: 16px; color: var(--ink);
  }
  /* back */
  .card--back {
    left: 300px; top: 472px;
    background: var(--white);
  }
  .back-band {
    position: absolute; left: 0; top: 0;
    width: 100%; height: 172px;
    background: var(--orange);
    border-bottom: 4px solid var(--rule-blue);
  }
  .card--back .wordmark { top: 62px; }
  .back-foot {
    position: absolute; left: 0; bottom: 0;
    width: 100%; height: 14px;
    background: var(--orange);
  }
  .person {
    position: absolute;
    right: 345px; top: 238px;
    text-align: right;
  }
  .person__name { font-size: 30px; color: var(--accent-blue); line-height: 1.1; }
  .person__role { font-size: 18px; color: var(--text); }
  .divider {
    position: absolute;
    left: 274px; top: 192px;
    width: 2px; height: 150px;
    background: var(--rule-blue);
  }
  .contacts {
    position: absolute;
    left: 292px; top: 196px;
    list-style: none;
  }
  .contacts li {
    display: flex; align-items: center; gap: 12px;
    height: 36px;
    font-size: 17px; color: var(--text);
  }
  .icon { width: 18px; height: 18px; flex: none; }
</style>
</head>
<body>

  <section class="card card--front" aria-label="Card front">
    <div class="wordmark">veranode</div>
    <div class="front-web">
      <svg class="icon" viewBox="0 0 20 20" fill="none" stroke="#16181f" stroke-width="1.6">
        <circle cx="10" cy="10" r="8"/><ellipse cx="10" cy="10" rx="3.5" ry="8"/><path d="M2 10h16M3.5 6h13M3.5 14h13"/>
      </svg>
      <span>harborlinetrade.com</span>
    </div>
  </section>

  <section class="card card--back" aria-label="Card back">
    <div class="back-band"></div>
    <div class="wordmark">veranode</div>

    <div class="person">
      <p class="person__name">Elin Marsh</p>
      <p class="person__role">Managing Director</p>
    </div>

    <div class="divider"></div>

    <ul class="contacts">
      <li>
        <svg class="icon" viewBox="0 0 20 20" fill="none" stroke="#2b7fc1" stroke-width="1.6">
          <path d="M5 2l3 4-2 2c1 2.5 3.5 5 6 6l2-2 4 3-2 3C9 18 2 11 2 5z"/>
        </svg>
        <span>614 207 835</span>
      </li>
      <li>
        <svg class="icon" viewBox="0 0 20 20" fill="#2b7fc1">
          <rect x="5" y="2" width="10" height="5"/><rect x="2" y="7" width="16" height="7" rx="1"/><rect x="5" y="12" width="10" height="6" fill="#fff" stroke="#2b7fc1" stroke-width="1.5"/>
        </svg>
        <span>614 380 2269</span>
      </li>
      <li>
        <svg class="icon" viewBox="0 0 20 20" fill="none" stroke="#2b7fc1" stroke-width="1.6">
          <circle cx="10" cy="10" r="8"/><ellipse cx="10" cy="10" rx="3.5" ry="8"/><path d="M2 10h16M3.5 6h13M3.5 14h13"/>
        </svg>
        <span>harborlinetrade.com</span>
      </li>
      <li>
        <svg class="icon" viewBox="0 0 20 20">
          <rect x="1" y="4" width="18" height="12" fill="#2b7fc1"/><path d="M1 4l9 7 9-7" fill="none" stroke="#fff" stroke-width="1.5"/>
        </svg>
        <span>elin@harborlinetrade</span>
      </li>
    </ul>

    <div class="back-foot"></div>
  </section>

</body>
</html>
```